Business Card for Veltrano, a french tech company

Tech company
New technologies
Serious design
Dark theme

User info :
Name: Mathis CORLAVE
Position: Co-Founder & CEO
Tel: (+33) 6 58 24 90 37
Email: mathis@veltrano.io
Website: www.veltrano.io
Address: 17 rue des Tanneurs 69002 LYON

Attached is the business logo file.

```html
<!DOCTYPE html>
<html lang="fr">
<head>
<meta charset="utf-8">
<title>Veltrano — Carte de visite</title>
<link rel="stylesheet" href="https://fonts.googleapis.com/css2?family=Montserrat:wght@400;500;700&display=swap">
<style>
  :root {
    --backdrop: #dadada;
    --navy-top: #0b2d5e;
    --navy-bottom: #0e063b;
    --ink: #0f0a40;
    --white: #ffffff;
    --violet: #9a0cdc;
    --magenta: #e4059a;
  }
  * { margin: 0; padding: 0; box-sizing: border-box; }
  html, body { width: 1200px; height: 1200px; overflow: hidden; }
  body {
    position: relative;
    background: var(--backdrop);
    font-family: "Montserrat", Arial, sans-serif;
  }
  .card {
    position: absolute;
    top: 159px;
    width: 448px;
    height: 747px;
    border-radius: 30px;
    overflow: hidden;
  }
  .card-front {
    left: 131px;
    background: linear-gradient(180deg, var(--navy-top) 0%, var(--navy-bottom) 75%);
  }
  .front-wordmark {
    position: absolute;
    left: 357px;
    top: 394px;
    transform: translate(-50%, -50%) rotate(-90deg);
    color: var(--white);
    font-weight: 700;
    font-size: 92px;
    letter-spacing: 2px;
    white-space: nowrap;
    line-height: 1;
  }
  .card-back {
    left: 633px;
    background: linear-gradient(180deg, var(--navy-top) 0%, var(--navy-bottom) 80%);
  }
  .brand-panel {
    position: absolute;
    left: 0; top: 0;
    width: 100%;
    height: 352px;
    background: var(--white);
    display: flex;
    align-items: center;
    justify-content: center;
  }
  .brand-name {
    color: var(--ink);
    font-weight: 700;
    font-size: 52px;
    letter-spacing: 1px;
  }
  .holder-name {
    position: absolute;
    top: 392px;
    width: 100%;
    text-align: center;
    font-weight: 500;
    font-size: 33px;
    letter-spacing: -1px;
    background: linear-gradient(90deg, var(--violet), var(--magenta));
    -webkit-background-clip: text;
    background-clip: text;
    color: transparent;
  }
  .holder-role {
    position: absolute;
    top: 441px;
    width: 100%;
    text-align: center;
    color: var(--white);
    font-size: 21px;
    letter-spacing: 0.5px;
  }
  .divider {
    position: absolute;
    left: 97px;
    top: 486px;
    width: 257px;
    height: 2px;
    background: linear-gradient(90deg, var(--violet), var(--magenta));
  }
  .contact-list {
    list-style: none;
    position: absolute;
    left: 78px;
    top: 510px;
    color: var(--white);
    font-size: 24px;
  }
  .contact-item {
    display: flex;
    align-items: flex-start;
    height: 39px;
    line-height: 30px;
  }
  .contact-item.address { line-height: 28px; }
  .contact-icon {
    width: 28px;
    height: 28px;
    margin-right: 14px;
    flex: none;
    margin-top: 2px;
  }
</style>
</head>
<body>

<section class="card card-front">
  <div class="front-wordmark">VELTRANO</div>
</section>

<section class="card card-back">
  <div class="brand-panel">
    <span class="brand-name">Veltrano</span>
  </div>

  <h1 class="holder-name">MATHIS CORLAVE</h1>
  <p class="holder-role">CO-FOUNDER &amp; CEO</p>
  <div class="divider"></div>

  <svg width="0" height="0" style="position:absolute">
    <defs>
      <linearGradient id="icon-gradient" x1="0" y1="0" x2="1" y2="1">
        <stop offset="0" stop-color="#9a0cdc"/>
        <stop offset="1" stop-color="#e4059a"/>
      </linearGradient>
    </defs>
  </svg>

  <ul class="contact-list">
    <li class="contact-item">
      <svg class="contact-icon" viewBox="0 0 24 24"><path fill="url(#icon-gradient)" d="M6.6 10.8a15.1 15.1 0 0 0 6.6 6.6l2.2-2.2c.3-.3.7-.4 1-.2 1.1.4 2.3.6 3.6.6.6 0 1 .4 1 1V20c0 .6-.4 1-1 1A17 17 0 0 1 3 4c0-.6.4-1 1-1h3.5c.6 0 1 .4 1 1 0 1.3.2 2.5.6 3.6.1.3 0 .7-.2 1z"/></svg>
      <span>(+33) 6 58 24 90 37</span>
    </li>
    <li class="contact-item">
      <svg class="contact-icon" viewBox="0 0 24 24"><path fill="url(#icon-gradient)" d="M2 6h20v12H2z"/><path fill="none" stroke="#0c1a4e" stroke-width="1.6" d="M2 6l10 7 10-7M2 18l7.5-6M22 18l-7.5-6"/></svg>
      <span>mathis@veltrano.io</span>
    </li>
    <li class="contact-item">
      <svg class="contact-icon" viewBox="0 0 24 24"><g fill="none" stroke="url(#icon-gradient)" stroke-width="1.6"><circle cx="12" cy="12" r="10"/><ellipse cx="12" cy="12" rx="4.5" ry="10"/><path d="M2 12h20M4 7h16M4 17h16M12 2v20"/></g></svg>
      <span>www.veltrano.io</span>
    </li>
    <li class="contact-item address">
      <svg class="contact-icon" viewBox="0 0 24 24"><path fill="url(#icon-gradient)" d="M12 2a7 7 0 0 0-7 7c0 5 7 13 7 13s7-8 7-13a7 7 0 0 0-7-7zm0 10.5a3.5 3.5 0 1 1 0-7 3.5 3.5 0 0 1 0 7z"/></svg>
      <span>17 rue des Tanneurs<br>69002&nbsp; LYON</span>
    </li>
  </ul>
</section>

</body>
</html>
```